Dental specialist needs a sharp looking letterhead

I am looking for a letterhead to be used to send letters and communication between myself (a dental specialist) and other dentists.
My office is a state of the art dental specialty office.
I need to letterhead to also state:
Gideon R. Whitfield DDS
2847 Birchmont Avenue, Suite K
West Harlow, NY 14391
(716)482-9163
fax: (716)482-9170
whitfieldroot.com (**this email address may change)

i included my logo designs.
thank you

Target Market(s)

dentists

Industry/Entity Type

Communication

Requirements
Must have
• the included logo, whether the vertical or horizontal versions

```html
<!DOCTYPE html>
<html lang="en">
<head>
<meta charset="utf-8">
<title>Keystone Endodontics P.C. – Letterhead</title>
<link href="https://fonts.googleapis.com/css2?family=Merriweather:wght@300;400&display=swap" rel="stylesheet">
<style>
  :root {
    --ink: #1b1b1b;
    --ink-soft: #444a4f;
    --brand-blue: #3ea3dc;
    --brand-green: #8cc63f;
    --paper: #ffffff;
    --icon-navy: #1e3550;
  }
  * { box-sizing: border-box; margin: 0; padding: 0; }
  html, body {
    width: 931px; height: 1200px; overflow: hidden;
    background: var(--paper);
    font-family: "Merriweather", Georgia, serif;
  }
  .letterhead { position: relative; width: 931px; height: 1200px; background: var(--paper); }

  .brand {
    position: absolute; left: 36px; top: 44px;
    display: flex; align-items: center; gap: 14px;
    color: var(--ink); font-weight: 400;
  }
  .brand__dot { width: 46px; height: 46px; border-radius: 50%; background: var(--brand-blue); flex: none; }
  .brand__name { font-size: 34px; line-height: 1; letter-spacing: -0.5px; }
  .brand__sub { display: block; font-size: 14px; letter-spacing: 2.5px; margin-top: 6px; padding-left: 28px; }

  .doctor {
    position: absolute; right: 36px; top: 30px;
    text-align: right; font-weight: 300;
  }
  .doctor__name { font-size: 20px; color: var(--brand-blue); letter-spacing: -0.3px; }
  .doctor__name .credential { color: var(--brand-green); }
  .doctor__line {
    display: flex; justify-content: flex-end; align-items: center; gap: 6px;
    font-size: 15px; color: var(--ink-soft); margin-top: 6px;
  }
  .doctor__line svg { flex: none; }

  .footer-rule { position: absolute; left: 0; right: 0; top: 1127px; height: 5px; background: var(--brand-blue); }
  .footer-band {
    position: absolute; left: 0; right: 0; top: 1136px; height: 60px;
    background: var(--brand-green); color: #fff; font-weight: 300;
    display: flex; flex-direction: column; align-items: center; justify-content: center; gap: 4px;
    font-size: 16px; letter-spacing: -0.3px;
  }
  .footer-band__line { display: flex; align-items: center; gap: 6px; }
</style>
</head>
<body>
<main class="letterhead">
  <header>
    <div class="brand">
      <span class="brand__dot"></span>
      <div>
        <span class="brand__name">KEYSTONE</span>
        <span class="brand__sub">Endodontics P.C.</span>
      </div>
    </div>

    <address class="doctor" style="font-style:normal">
      <p class="doctor__name">Gideon R. Whitfield, <span class="credential">DDS</span></p>
      <p class="doctor__line">
        <svg width="14" height="14" viewBox="0 0 14 14" aria-hidden="true"><circle cx="7" cy="7" r="6" fill="none" stroke="#444a4f" stroke-width="1.2"/><path d="M5 3.5c-1 1-1 3.5 1 5.5s4 2.4 5 1.3l-1.3-1.4-1 .6C7.5 9 5.6 7 5.3 6l.6-1z" fill="#444a4f"/></svg>
        716-482-9163
      </p>
      <p class="doctor__line">
        <svg width="14" height="10" viewBox="0 0 14 10" aria-hidden="true"><rect width="14" height="10" fill="var(--icon-navy)"/><path d="M0 0l7 5 7-5" fill="none" stroke="#fff" stroke-width="1.2"/></svg>
        office@whitfieldroot.com
      </p>
    </address>
  </header>

  <footer>
    <div class="footer-rule"></div>
    <div class="footer-band">
      <p class="footer-band__line">
        <svg width="16" height="13" viewBox="0 0 16 13" aria-hidden="true"><rect x="4" y="0" width="8" height="4" fill="#fff"/><rect x="0" y="4" width="16" height="6" rx="1.5" fill="#fff"/><rect x="3" y="8" width="10" height="5" fill="#fff" stroke="#8cc63f" stroke-width="1"/></svg>
        716-482-9170
      </p>
      <p class="footer-band__line">
        <svg width="12" height="16" viewBox="0 0 12 16" aria-hidden="true"><path d="M6 0a6 6 0 0 0-6 6c0 4.5 6 10 6 10s6-5.5 6-10a6 6 0 0 0-6-6zm0 8.5A2.5 2.5 0 1 1 6 3.5a2.5 2.5 0 0 1 0 5z" fill="#fff"/></svg>
        2847 Birchmont Avenue, Suite K, West Harlow, NY 14391
      </p>
    </div>
  </footer>
</main>
</body>
</html>
```